Business Card

Can you please copy the format provided for the business cards.
Can the logo be in the colours of the last file as specified.

Can the text please be in grey

• Navy Blue: #00457C
• Grey Text: #555555
• Orange Text: #FDBF29

The names on the business card will be

Dorian Platt
0452 718 340
dorian.platt@ridgelineassetlending.com.au

Lvl 7, 14 Harbourview Pde
Merrivale QLD 4290
PO Box 3472
Tarrin Vale MC QLD 9781
P: 1300 462 519
F: 1300 462 538
www.ridgelineassetlending.com.au

And

Liam Hollis
0437 915 604
liam.hollis@ridgelineassetlending.com.au

Lvl 7, 14 Harbourview Pde
Merrivale QLD 4290
PO Box 3472
Tarrin Vale MC QLD 9781
P: 1300 462 519
F: 1300 471 926

Industry/Entity Type

Business

```html
<!DOCTYPE html>
<html lang="en">
<head>
<meta charset="utf-8">
<title>Ridgeline Asset Lending – Business Card</title>
<link href="https://fonts.googleapis.com/css2?family=Ubuntu:wght@400;700&family=Ubuntu+Condensed&display=swap" rel="stylesheet">
<style>
  :root {
    --navy: #00457C;
    --grey-text: #555555;
    --orange: #FDBF29;
    --backdrop: #e6e6e6;
    --card: #ffffff;
    --faint-blue: #e4ecf5;
    --rule: #3a3a3a;
  }
  html, body {
    margin: 0;
    padding: 0;
    overflow: hidden;
  }
  body {
    width: 1200px;
    height: 1096px;
    background: var(--backdrop);
    position: relative;
    font-family: "Ubuntu", sans-serif;
    color: var(--grey-text);
  }
  .card {
    position: absolute;
    left: 196px;
    width: 807px;
    height: 459px;
    background: var(--card);
    overflow: hidden;
  }
  .card--front { top: 63px; }
  .card--back { top: 572px; }
  .band {
    position: absolute;
    left: 0;
    width: 100%;
    height: 12px;
    background: var(--navy);
  }
  .band--top { top: 0; }
  .band--bottom { bottom: 0; }

  .brand {
    position: absolute;
    display: flex;
    align-items: center;
    gap: 14px;
    white-space: nowrap;
  }
  .brand__square {
    width: 30px;
    height: 30px;
    background: var(--navy);
    flex: none;
  }
  .brand__name {
    font-weight: 700;
    color: var(--navy);
    letter-spacing: 0.2px;
  }
  .card--front .brand { left: 69px; top: 84px; }
  .card--front .brand__name { font-size: 28px; }

  .contact {
    position: absolute;
    left: 69px;
    top: 322px;
    line-height: 1;
  }
  .contact__name, .contact__mobile {
    font-size: 23px;
    margin: 0 0 6px;
  }
  .contact__email {
    font-size: 17px;
    margin: 8px 0 0;
  }

  .watermark {
    position: absolute;
    left: 240px;
    top: 60px;
    width: 280px;
    height: 280px;
    background: var(--faint-blue);
  }
  .card--back .brand { left: 41px; top: 206px; }
  .card--back .brand__name { font-size: 27px; }

  .divider {
    position: absolute;
    left: 428px;
    top: 65px;
    width: 2px;
    height: 330px;
    background: var(--rule);
  }
  .office {
    position: absolute;
    left: 467px;
    top: 129px;
    font-size: 21px;
    line-height: 25px;
  }
  .office p { margin: 0 0 9px; }
  .office__web {
    font-family: "Ubuntu Condensed", sans-serif;
    font-size: 19px;
    margin-top: 12px !important;
  }
</style>
</head>
<body>
  <section class="card card--front">
    <div class="band band--top"></div>
    <div class="brand">
      <span class="brand__square"></span>
      <span class="brand__name">Ridgeline Asset Lending</span>
    </div>
    <div class="contact">
      <p class="contact__name">Dorian Platt</p>
      <p class="contact__mobile">0452 718 340</p>
      <p class="contact__email">dorian.platt@ridgelineassetlending.com.au</p>
    </div>
    <div class="band band--bottom"></div>
  </section>

  <section class="card card--back">
    <div class="band band--top"></div>
    <div class="watermark"></div>
    <div class="brand">
      <span class="brand__name">Ridgeline Asset Lending</span>
      <span class="brand__square"></span>
    </div>
    <div class="divider"></div>
    <div class="office">
      <p>Lvl 7, 14 Harbourview Pde<br>Merrivale QLD 4290</p>
      <p>PO Box 3472<br>Tarrin Vale MC QLD 9781</p>
      <p>P: 1300 462 519<br>F: 1300 462 538</p>
      <p class="office__web">www.ridgelineassetlending.com.au</p>
    </div>
    <div class="band band--bottom"></div>
  </section>
</body>
</html>
```